Clausewise - Training I Consulting I Review - Related to Contracts/Agreements

We provide legal services, we need a plattform to book video online trainings or local trainings classes and appointments (with calendar feature to select date and see availability at screen), payment over internet, legal document creation over webpage, videos will be produces in the next 3 - 4 moths so this is a place holder item. Participants for the Online trainings shall have a login in area with secured password. Appointments for local trainings and Consulting. Consider Outline in file attached. I can send you also a video with more explanation regarding the purpose.

Target Market(s)

Startup/scale up Software companies that intent to have an international business and need help with their contracts, to sell their products. Sales persons.

Industry/Entity Type

Legal

Coding

Coded - Design and coding required

Number of Pages Required

5+ page

Font styles to use
Serif
Sans Serif

Colors
000000
eeeeee
f5f5f5
ffffff
f8fcfd
3277b5
ecf7fb
cadf82
86cfc6

Requirements
Must have
• See file clausewise attached with outline. Moreover see here first starting point: https://tomas-vendrell.pagebuildr.example/mysite-1 . Main inspiration comes from www.advisoryhub.example from the log in area, see the outline in the file attached with the screen shots. At the end I need someone who can draft the full webpage and maintain it for a yearly fee. It must be simple and well structured layout. Lean. 1st landing page shall not scroll, 2 landing page only a little to see the testimonials and foster of page. There should be a Progress Bar to indicate the booking/selection process. Calendar booking. Easy fast booking.
• I like the colour mix, the feeling and the easy structor of:
• https://www.artmarket.example/design/6374387or
• https://www.artmarket.example/design/6372391 or https://www.artmarket.example/design/6374366
• https://www.vendorgrid.example/en/web-design/belgium-be
• https://www.artmarket.example/design/5896857
• https://www.artmarket.example/design/5902173
• https://www.artmarket.example/design/17197349
• https://www.artmarket.example/design/5464461
• https://www.artmarket.example/design/7180908
Nice to have
• page for evaluation and interview, see outline attached in the file with screen shots. Document upload.
Should not have
• many pictures, long scroll down pages on the 1st and 2nd ladding pages, many colours and forms. No need for news letter, search field, no need for links to Chatterly and other social media (except workNet).

```html
<!DOCTYPE html>
<html lang="en">
<head>
<meta charset="utf-8">
<title>Clausewise – Contracts Training, Consulting and Review</title>
<link href="https://fonts.googleapis.com/css2?family=Lato:wght@400;700&family=Poppins:wght@500&display=swap" rel="stylesheet">
<style>
  :root {
    --canvas: #e6e6e6;
    --white: #ffffff;
    --ink: #222222;
    --text: #444444;
    --muted: #555555;
    --red: #e8202a;
    --dark-btn: #333333;
    --band: #f4f4f4;
    --lime: #c9dd7f;
    --footer-dark: #232323;
    --card-shadow: 0 1px 4px rgba(0,0,0,0.22);
  }
  * { box-sizing: border-box; margin: 0; padding: 0; }
  html, body { width: 1200px; height: 1039px; overflow: hidden; }
  body { background: var(--canvas); font-family: "Lato", sans-serif; color: var(--text); position: relative; }

  .page { position: absolute; background: var(--white); box-shadow: 0 1px 5px rgba(0,0,0,0.25); overflow: hidden; }
  .home { left: 30px; top: 60px; width: 560px; height: 918px; }
  .splash { left: 606px; top: 60px; width: 560px; height: 315px; }

  /* Home hero */
  .hero { position: absolute; left: 0; top: 0; width: 560px; height: 247px;
    background: linear-gradient(135deg, #5a4a3c 0%, #3f352d 45%, #6b5846 75%, #3a302a 100%); }
  .hero-shade { position: absolute; inset: 0; background: rgba(20,18,16,0.35); }
  .nav { position: absolute; left: 46px; top: 0; width: 468px; height: 45px; border-bottom: 1.5px solid rgba(255,255,255,0.85);
    display: flex; align-items: center; }
  .brand { font-family: "Lato", sans-serif; font-weight: 400; color: var(--white); font-size: 18px; letter-spacing: 0.5px; }
  .nav-links { margin-left: auto; display: flex; align-items: center; gap: 0; list-style: none; }
  .nav-links li { font-size: 7.5px; font-weight: 700; color: var(--white); text-transform: uppercase; margin-left: 28px; letter-spacing: 0.2px; }
  .nav-links li:first-child { margin-left: 0; }
  .nav-links .login { border: 1.2px solid var(--white); padding: 5px 10px; margin-left: 15px; }
  .hero-title { position: absolute; left: 0; width: 100%; top: 84px; text-align: center; font-family: "Poppins", sans-serif; font-weight: 500;
    font-size: 31px; color: var(--white); letter-spacing: -0.3px; }
  .hero-lead { position: absolute; left: 100px; width: 360px; top: 142px; text-align: center; font-size: 8.5px; line-height: 13px; color: var(--white); }
  .dots { position: absolute; top: 222px; left: 0; width: 100%; display: flex; justify-content: center; gap: 3px; }
  .dots span { width: 9px; height: 9px; border-radius: 50%; background: rgba(255,255,255,0.55); }
  .dots span.active { background: var(--white); }

  .section-title { position: absolute; left: 0; width: 100%; text-align: center; color: var(--red); font-weight: 700; font-size: 15.5px; }
  .section-rule { position: absolute; left: 248px; width: 62px; height: 1.5px; background: var(--red); }

  /* Services */
  .service-card { position: absolute; top: 341px; width: 146px; height: 162px; background: var(--white); box-shadow: var(--card-shadow);
    text-align: center; }
  .service-card svg { position: absolute; top: 13px; left: 58px; }
  .service-card h3 { position: absolute; top: 51px; width: 100%; font-size: 9px; font-weight: 400; color: var(--ink); letter-spacing: 0.2px; }
  .service-card .rule { position: absolute; top: 70px; left: 55px; width: 36px; height: 1px; background: var(--ink); }
  .service-card p { position: absolute; top: 81px; left: 7px; width: 132px; font-size: 6.3px; line-height: 9.7px; color: var(--muted); }
  .service-card .btn { position: absolute; top: 129px; left: 50%; transform: translateX(-50%); background: var(--dark-btn); color: var(--white);
    font-size: 7.5px; padding: 4px 8px; border-radius: 2px; white-space: nowrap; }
  .service-card.featured h3 { color: var(--red); }
  .service-card.featured .rule { background: var(--red); }
  .service-card.featured .btn { background: var(--red); }

  /* Testimonials */
  .testimonials { position: absolute; left: 0; top: 546px; width: 560px; height: 228px; background: var(--band); }
  .quote-card { position: absolute; top: 96px; width: 146px; height: 87px; background: var(--white); box-shadow: var(--card-shadow); }
  .avatar { position: absolute; left: 5px; top: 14px; width: 33px; height: 33px; border-radius: 50%; background: linear-gradient(160deg, #8a6d5a, #4a3b31); }
  .stars { position: absolute; left: 45px; top: 16px; }
  .quote-card p { position: absolute; left: 45px; top: 32px; width: 94px; font-size: 6.3px; line-height: 9px; color: var(--muted); text-align: justify; }
  .quote-card cite { position: absolute; left: 45px; top: 65px; font-style: normal; font-size: 6.8px; color: var(--red); }

  /* Footer */
  .site-footer .brand { position: absolute; left: 0; width: 100%; top: 802px; text-align: center; color: var(--ink); font-size: 22px; }
  .footer-links { position: absolute; top: 847px; left: 0; width: 100%; text-align: center; font-size: 7.5px; color: var(--ink); font-weight: 700; list-style: none; }
  .footer-links li { display: inline; }
  .footer-links li + li::before { content: "|"; font-weight: 400; margin: 0 6px 0 5px; }
  .footer-rule { position: absolute; left: 46px; top: 876px; width: 468px; height: 1px; background: var(--ink); }
  .legal { position: absolute; top: 894px; left: 0; width: 100%; text-align: center; font-size: 7px; color: var(--ink); }
  .code { position: absolute; top: 894px; right: 19px; font-size: 7px; color: var(--ink); }

  /* Splash */
  .splash-bg { position: absolute; left: 0; top: 0; width: 560px; height: 289px;
    background: linear-gradient(100deg, #5b6368 0%, #3b4348 30%, #6f777b 55%, #3a4146 80%, #555d61 100%); }
  .splash-shade { position: absolute; inset: 0; background: rgba(25,30,34,0.3); }
  .brand-block { position: absolute; left: 208px; top: 41px; width: 144px; height: 70px; background: var(--lime);
    display: flex; align-items: center; justify-content: center; }
  .brand-block .brand { font-size: 22px; }
  .splash h2 { position: absolute; top: 133px; width: 100%; text-align: center; color: var(--white); font-weight: 700; font-size: 18px; }
  .offer { position: absolute; top: 168px; left: 0; width: 100%; display: flex; justify-content: center; list-style: none;
    color: var(--white); font-weight: 700; font-size: 18.5px; }
  .offer li { margin: 0 6px; }
  .offer li::before { content: "•"; margin-right: 7px; }
  .enter { position: absolute; left: 249px; top: 214px; width: 62px; height: 26px; border: 1.2px solid var(--white); color: var(--white);
    font-size: 10px; display: flex; align-items: center; justify-content: center; letter-spacing: 0.3px; }
  .splash-footer { position: absolute; left: 0; top: 289px; width: 560px; height: 26px; background: var(--footer-dark); border-top: 1px solid #888; }
  .splash-footer .legal { top: 8px; color: var(--white); }
  .splash-footer .code { top: 8px; color: var(--white); }
</style>
</head>
<body>

<main class="page home">
  <header class="hero">
    <div class="hero-photo" role="img" aria-label="Photo of a team meeting around an office table" style="position:absolute;inset:0;"></div>
    <div class="hero-shade"></div>
    <nav class="nav">
      <span class="brand">Clausewise</span>
      <ul class="nav-links">
        <li>Refer Someone</li>
        <li>Services</li>
        <li>Partner</li>
        <li>Contact</li>
        <li class="login">Login</li>
      </ul>
    </nav>
    <h1 class="hero-title">Clausewise</h1>
    <p class="hero-lead">Nemo enim ipsam voluptatem quia voluptas sit aspernatur aut odit aut fugit, sed quia consequun tur magni dolores eos qui ratione voluptatem.</p>
    <div class="dots"><span class="active"></span><span></span><span></span><span></span><span></span></div>
  </header>

  <section class="services">
    <h2 class="section-title" style="top:281px;">CHOOSE YOUR SERVICE</h2>
    <div class="section-rule" style="top:309px;"></div>

    <article class="service-card" style="left:46px;">
      <svg width="30" height="28" viewBox="0 0 30 28" fill="none" stroke="#333" stroke-width="1.4">
        <rect x="2" y="1" width="26" height="2" fill="#333"/>
        <rect x="3" y="3" width="24" height="14"/>
        <line x1="8" y1="7" x2="22" y2="7"/><line x1="8" y1="10" x2="22" y2="10"/><line x1="8" y1="13" x2="18" y2="13"/>
        <circle cx="7" cy="20" r="2"/><circle cx="15" cy="20" r="2"/><circle cx="23" cy="20" r="2"/>
        <path d="M3 27v-3h8v3M11 27v-3h8v3M19 27v-3h8v3"/>
      </svg>
      <h3>CONTRACT TRAINING</h3>
      <div class="rule"></div>
      <p>Nemo enim ipsam voluptatem quia voluptas sit aspernatur aut odit aut fugit, sed quia conse quuntur magni dolores eos qui ratione volupta tem sequi nesciunt.</p>
      <span class="btn">BOOK</span>
    </article>

    <article class="service-card featured" style="left:207px;">
      <svg width="30" height="30" viewBox="0 0 30 30" fill="#e8202a">
        <circle cx="15" cy="8" r="7"/>
        <rect x="11" y="6" width="8" height="1.3" fill="#fff"/><rect x="11" y="9" width="6" height="1.3" fill="#fff"/>
        <circle cx="7" cy="20" r="3"/><path d="M2 29c0-4 2.5-6 5-6s5 2 5 6z"/>
        <circle cx="23" cy="20" r="3"/><path d="M18 29c0-4 2.5-6 5-6s5 2 5 6z"/>
      </svg>
      <h3>CONTRACT CONSULTING</h3>
      <div class="rule"></div>
      <p>Nemo enim ipsam voluptatem quia voluptas sit aspernatur aut odit aut fugit, sed quia conse quuntur magni dolores eos qui ratione volupta tem sequi nesciunt.</p>
      <span class="btn">APPOINTMENT</span>
    </article>

    <article class="service-card" style="left:368px;">
      <svg width="30" height="28" viewBox="0 0 30 28" fill="none" stroke="#333" stroke-width="1.3">
        <rect x="1" y="1" width="18" height="11"/>
        <line x1="4" y1="4" x2="16" y2="4"/><line x1="4" y1="7" x2="16" y2="7"/><line x1="4" y1="10" x2="12" y2="10"/>
        <rect x="12" y="7" width="17" height="10" fill="#fff"/>
        <line x1="15" y1="10" x2="26" y2="10"/><line x1="15" y1="13" x2="26" y2="13"/>
        <path d="M7 20l1.2 2.4 2.6.3-1.9 1.8.5 2.6L7 25.8 4.6 27.1l.5-2.6-1.9-1.8 2.6-.3z" fill="#333" stroke="none"/>
        <path d="M15 20l1.2 2.4 2.6.3-1.9 1.8.5 2.6L15 25.8l-2.4 1.3.5-2.6-1.9-1.8 2.6-.3z" fill="#333" stroke="none"/>
        <path d="M23 20l1.2 2.4 2.6.3-1.9 1.8.5 2.6L23 25.8l-2.4 1.3.5-2.6-1.9-1.8 2.6-.3z" fill="#333" stroke="none"/>
      </svg>
      <h3>CONTRACT REVIEW</h3>
      <div class="rule"></div>
      <p>Nemo enim ipsam voluptatem quia voluptas sit aspernatur aut odit aut fugit, sed quia conse quuntur magni dolores eos qui ratione volupta tem sequi nesciunt.</p>
      <span class="btn">REQUEST</span>
    </article>
  </section>

  <section class="testimonials">
    <h2 class="section-title" style="top:29px;">OUR TESTIMONIALS</h2>
    <div class="section-rule" style="top:57px;"></div>

    <article class="quote-card" style="left:46px;">
      <div class="avatar" role="img" aria-label="Portrait photo of Madrin"></div>
      <svg class="stars" width="52" height="9" viewBox="0 0 52 9" fill="#e8202a">
        <path id="star" d="M4.5 0l1.1 3.2H9L6.3 5.1l1 3.3-2.8-2-2.8 2 1-3.3L0 3.2h3.4z"/>
        <use href="#star" x="10.5"/><use href="#star" x="21"/><use href="#star" x="31.5"/><use href="#star" x="42"/>
      </svg>
      <p>Nemo enim ipsam voluptatem quia voluptas sit aspernatur aut odit aut fugit, sed.</p>
      <cite>Madrin, Manager</cite>
    </article>

    <article class="quote-card" style="left:207px;">
      <div class="avatar" role="img" aria-label="Portrait photo of Anne"></div>
      <svg class="stars" width="52" height="9" viewBox="0 0 52 9" fill="#e8202a">
        <use href="#star"/><use href="#star" x="10.5"/><use href="#star" x="21"/><use href="#star" x="31.5"/><use href="#star" x="42"/>
      </svg>
      <p>Nemo enim ipsam voluptatem quia voluptas sit aspernatur aut odit aut fugit, sed.</p>
      <cite>Anne, Manager</cite>
    </article>

    <article class="quote-card" style="left:368px;">
      <div class="avatar" role="img" aria-label="Portrait photo of John"></div>
      <svg class="stars" width="52" height="9" viewBox="0 0 52 9" fill="#e8202a">
        <use href="#star"/><use href="#star" x="10.5"/><use href="#star" x="21"/><use href="#star" x="31.5"/><use href="#star" x="42"/>
      </svg>
      <p>Nemo enim ipsam voluptatem quia voluptas sit aspernatur aut odit aut fugit, sed.</p>
      <cite>John, Manager</cite>
    </article>
  </section>

  <footer class="site-footer">
    <span class="brand">Clausewise</span>
    <ul class="footer-links">
      <li>Evaluation</li><li>Students</li><li>Policies</li><li>Team</li><li>Market</li><li>Feedback</li><li>Templates</li><li>Tools</li><li>Contact</li>
    </ul>
    <div class="footer-rule"></div>
    <p class="legal">Copyrights @ 2018 Clausewise. All Rights Reserved.</p>
    <span class="code">C20</span>
  </footer>
</main>

<section class="page splash">
  <div class="splash-bg" role="img" aria-label="Motion-blurred photo of business people walking through a hall"></div>
  <div class="splash-shade"></div>
  <div class="brand-block"><span class="brand">Clausewise</span></div>
  <h2>CONTRACTS</h2>
  <ul class="offer">
    <li>TRAINING</li>
    <li>CONSULTING</li>
    <li>DESIGN</li>
  </ul>
  <span class="enter">ENTER</span>
  <footer class="splash-footer">
    <p class="legal">Copyrights @ 2018 Clausewise. All Rights Reserved.</p>
    <span class="code">C20</span>
  </footer>
</section>

</body>
</html>
```